Hospitality project presentation

I am developing a hospitality project and I need to present to the developer an outstanding presentation highlighting the overall look and feel. I will provide the text and most of the pictures (not all of them) some pictures (copyright free) will hae to be provided by the designer. Maximum number of pages 15, and zoom calls with me to make some adjustment if needed.

Industry/Entity Type

Hospitality

Font styles to use
Other font styles liked:
• calibri light

Requirements
Must have
• 15 slides
Nice to have
• Hospitality resort project look and feel

```html
<!DOCTYPE html>
<html lang="en">
<head>
<meta charset="utf-8">
<title>Hospitality Presentation – Slide Overview</title>
<link rel="stylesheet" href="https://fonts.googleapis.com/css2?family=Hanken+Grotesk:wght@300;400;600;700&display=swap">
<style>
  :root {
    --board: #4b4b4b;
    --ink-dark: #191919;
    --ink-black: #0f0f0f;
    --gold: #d2b033;
    --paper: #e6e7e8;
    --white: #ffffff;
    --text-light: #d8d8d8;
    --text-dark: #222222;
  }
  * { margin: 0; padding: 0; box-sizing: border-box; }
  html, body { width: 1200px; height: 741px; overflow: hidden; background: var(--board); }
  body { font-family: "Hanken Grotesk", "Calibri", sans-serif; }
  .canvas { width: 1200px; height: 741px; overflow: hidden; position: relative; }
  .board {
    position: absolute; left: 0; top: 0; width: 1214px; height: 750px;
    transform: scale(0.98847); transform-origin: 0 0; background: var(--board);
  }
  .slide { position: absolute; overflow: hidden; }
  .abs { position: absolute; }
  .photo { position: absolute; }

  /* Slide: introduction */
  .slide-intro { left: 0; top: 0; width: 920px; height: 308px; background: var(--ink-dark); color: var(--text-light); }
  .body-small { font-size: 8px; line-height: 12px; }
  .intro-col-left { left: 31px; top: -4px; width: 180px; }
  .intro-col-left p + p { margin-top: 8px; }
  .stat-box { left: 31px; top: 128px; width: 178px; height: 180px; background: var(--gold); color: var(--ink-black); padding: 40px 32px; }
  .stat-figure { margin-top: 8px; font-size: 15px; font-weight: 700; color: var(--white); }
  .stat-rule { width: 40px; height: 3px; background: var(--ink-black); margin: 4px 0 6px; }
  .stat-label { font-size: 8px; font-weight: 600; }
  .intro-col-mid { left: 298px; top: -4px; width: 165px; }
  .intro-heading { margin-top: 30px; font-size: 11px; line-height: 13px; font-weight: 700; color: var(--white); margin-bottom: 6px; }
  .intro-col-mid p + p { margin-top: 8px; }
  .intro-bullet { left: 266px; top: 50px; }
  .intro-photo { left: 519px; top: 0; width: 401px; height: 308px; background: linear-gradient(160deg, #c9c4bc 0%, #8a847c 45%, #5d5750 75%, #3d3a37 100%); }
  .slide-footer { left: 519px; top: 276px; width: 401px; height: 19px; background: var(--ink-black); color: var(--white); font-size: 10px; letter-spacing: .3px; }
  .footer-trail { position: absolute; right: 55px; top: 3px; }
  .footer-trail strong { font-weight: 700; }
  .footer-number { position: absolute; right: 2px; top: 0; width: 39px; height: 19px; background: var(--gold); font-weight: 700; text-align: center; line-height: 19px; }

  /* Slide: section title */
  .slide-section { left: 950px; top: 0; width: 264px; height: 308px; }
  .section-photo { inset: 0; background: linear-gradient(135deg, #f4f3f1 0%, #dcd9d5 55%, #c3bfba 100%); }
  .section-band { left: 0; top: 252px; width: 264px; height: 56px; background: rgba(255,255,255,.35); }
  .section-title { left: 96px; top: 106px; font-size: 34px; font-weight: 300; color: var(--ink-black); white-space: nowrap; letter-spacing: .5px; }

  /* Slide: gallery grid */
  .slide-gallery { left: 0; top: 338px; width: 920px; height: 412px; background: var(--paper); }
  .tile { width: 200px; }
  .tile-top { top: 65px; height: 199px; }
  .tile-bottom { top: 274px; height: 140px; }
  .wood-a { background: linear-gradient(150deg, #c8c23a 0%, #6f4a25 55%, #3b2414 100%); }
  .wood-b { background: linear-gradient(160deg, #d9d6d2 0%, #9d8c78 45%, #5a3a20 100%); }
  .wood-c { background: linear-gradient(170deg, #ece9e5 0%, #7d5330 45%, #4f3019 100%); }
  .wood-d { background: linear-gradient(160deg, #bdb5ab 0%, #8a6a48 50%, #d8d4cf 100%); }
  .wood-e { background: linear-gradient(170deg, #cfc8bf 0%, #70482a 50%, #b9b2aa 100%); }
  .stair { background: linear-gradient(160deg, #f2f0ec 0%, #d8d1c8 50%, #6b4a30 100%); }
  .gallery-title-box { left: 659px; top: 0; width: 200px; height: 210px; background: var(--gold); color: var(--white); font-size: 23px; line-height: 32px; font-weight: 300; text-align: right; padding: 62px 57px 0 0; }
  .gallery-text { left: 258px; top: 308px; width: 160px; color: var(--text-dark); }
  .gold-lead { color: var(--gold); font-weight: 700; font-size: 13px; line-height: 15px; margin-bottom: 8px; }

  /* Slide: dark feature */
  .slide-feature { left: 950px; top: 338px; width: 264px; height: 412px; background: #1c1c1c; }
  .feature-photo { inset: 0; background: linear-gradient(170deg, #2b2a28 0%, #1a1a1a 60%, #262523 100%); }
  .feature-text { left: 79px; top: 176px; width: 150px; color: var(--white); }
  .feature-text .gold-lead { font-size: 12.5px; line-height: 18px; margin-bottom: 10px; }
  .feature-text p + p { margin-top: 6px; }
  .roof-line { overflow: visible; }
</style>
</head>
<body>
<div class="canvas">
  <div class="board">

    <section class="slide slide-intro">
      <div class="abs intro-col-left body-small">
        <p>adipiscing elit. Mauris ipsum odio, vehicula ac venenatis at, maximus in dolor. Vivamus euismod venenatis aliquam.</p>
        <p>Maecenas posuere consequat lectus sed faucibus. Sed dignissim nunc vitae fringilla malesuada. Sed ac maximus diam. Aenean eget nibh sit amet tellus pharetra.</p>
      </div>
      <div class="abs stat-box">
        <svg width="28" height="34" viewBox="0 0 28 34" aria-hidden="true">
          <rect x="0" y="6" width="18" height="28" fill="#0f0f0f"/>
          <rect x="18" y="14" width="10" height="20" fill="#0f0f0f"/>
          <g fill="#d2b033">
            <rect x="3" y="10" width="3" height="3"/><rect x="8" y="10" width="3" height="3"/><rect x="13" y="10" width="3" height="3"/>
            <rect x="3" y="16" width="3" height="3"/><rect x="8" y="16" width="3" height="3"/><rect x="13" y="16" width="3" height="3"/>
            <rect x="3" y="22" width="3" height="3"/><rect x="8" y="22" width="3" height="3"/><rect x="13" y="22" width="3" height="3"/>
            <rect x="21" y="18" width="3" height="3"/><rect x="21" y="24" width="3" height="3"/>
          </g>
        </svg>
        <div class="stat-figure">00000+</div>
        <div class="stat-rule"></div>
        <div class="stat-label">Lorem ipsum dolor sit amet</div>
      </div>
      <svg class="abs intro-bullet" width="24" height="24" viewBox="0 0 24 24" aria-hidden="true"><circle cx="12" cy="12" r="12" fill="#d2b033"/></svg>
      <div class="abs intro-col-mid body-small">
        <p>lacus, pharetra quis faucibus nec, pellentesque in ex.</p>
        <h3 class="intro-heading">Vestibulum porta justo quis suscipit tempus.</h3>
        <p>Vestibulum porta justo quis suscipit tempus. Donec eu turpis id urna venenatis fermentum. Mauris ut condimentum nisi. Fusce aliquet nisl a lectus posuere malesuada scelerisque.</p>
        <p>Phasellus cursus felis id lacus fringilla, at pharetra nisl accumsan. Suspendisse luctus erat euismod orci iaculis venenatis. Nulla non maximus dui. Praesent bibendum a ante ut vulputate.</p>
      </div>
      <div class="photo intro-photo" role="img" aria-label="Hotel bedroom with upholstered bed and cushions"></div>
      <div class="abs slide-footer">
        <span class="footer-trail">Sample Hospitality Powerpoint &gt; <strong>Introdution</strong></span>
        <span class="footer-number">01</span>
      </div>
    </section>

    <section class="slide slide-section">
      <div class="photo section-photo" role="img" aria-label="Bright bathroom vanity with white cabinetry"></div>
      <div class="abs section-band"></div>
      <svg class="abs roof-line" style="left:98px;top:82px" width="170" height="14" viewBox="0 0 170 14" aria-hidden="true">
        <polyline points="0,13 17,2 34,13 170,13" fill="none" stroke="#d2b033" stroke-width="1.6"/>
      </svg>
      <h2 class="abs section-title">Section Title</h2>
    </section>

    <section class="slide slide-gallery">
      <div class="photo tile tile-top wood-a" style="left:19px" role="img" aria-label="Kitchen with wood cabinets and pendant light"></div>
      <div class="photo tile tile-top wood-b" style="left:229px" role="img" aria-label="Modern pendant light fixture over kitchen"></div>
      <div class="photo tile tile-top wood-c" style="left:439px" role="img" aria-label="Wood kitchen cabinetry with range hood"></div>
      <h2 class="abs gallery-title-box">Gallery<br>Grid +<br>Text</h2>
      <div class="photo tile tile-bottom wood-d" style="left:19px" role="img" aria-label="Kitchen island with bar stools"></div>
      <div class="abs gallery-text body-small">
        <p class="gold-lead">Lorem ipsum dolor sit amet, consectetur adipiscing elit.</p>
        <p>Vestibulum porta justo quis suscipit tempus. Donec eu turpis id urna venenatis fermentum. Mauris ut condimentum nisi. Fusce aliquet</p>
      </div>
      <div class="photo tile tile-bottom wood-e" style="left:439px" role="img" aria-label="Kitchen with built-in ovens and cooktop"></div>
      <div class="photo tile tile-bottom stair" style="left:649px" role="img" aria-label="Staircase with wood treads"></div>
    </section>

    <section class="slide slide-feature">
      <div class="photo feature-photo" role="img" aria-label="Dimly lit interior of the resort"></div>
      <svg class="abs roof-line" style="left:79px;top:80px" width="190" height="24" viewBox="0 0 190 24" aria-hidden="true">
        <polyline points="0,22 30,2 60,22 190,22" fill="none" stroke="#d2b033" stroke-width="1.8"/>
      </svg>
      <div class="abs feature-text body-small">
        <p class="gold-lead">Lorem ipsum dolor sit amet, consectetur adipiscing elit. Mauris ipsum odio, vehicula ac venenatis at, maximus in dolor.</p>
        <p>Vestibulum porta justo quis suscipit tempus. Donec eu turpis id urna venenatis fermentum. Mauris ut condimentum nisi. Fusce aliquet nisl a lectus posuere malesuada.</p>
        <p>Phasellus cursus felis id lacus fringilla, at pharetra nisl accumsan. Suspendisse luctus erat euismod orci iaculis venenatis. Nulla non maximus dui. Praesent</p>
      </div>
    </section>

  </div>
</div>
</body>
</html>
```